Adventure Business Cards

Please check out our website for style
Vertical card
Details:
Side 1
Logo
Business name: Kestrel Point Wildland Tours
Name: Colin Warbeck
Role: Director
Email: info@kestrelpointtours.com
Address: PO Box 71, Marlin Cove NSW 2471
Phone: +61 2 5550 1847
Web address: www.kestrelpointtours.com
Side 2
Taking pictures?
A Friendwall and Pixlane logo
Tag us in your pictures with
#kpwildtours
@kpwildtours
www.kestrelpointtours.com
Details:
Side 1
Logo
Name: Colin Warbeck
Role: Director
Phone: +61 2 5550 1847
Side 2
Taking pictures?
#kpwildtours
@kpwildtours

```html
<!DOCTYPE html>
<html lang="en">
<head>
<meta charset="utf-8">
<title>Kestrel Point Wildland Tours – Business Cards</title>
<link rel="stylesheet" href="https://fonts.googleapis.com/css2?family=Delius&family=Oxygen:wght@300;400&display=swap">
<style>
  :root {
    --backdrop: #ecebea;
    --card-blue: #2f86c0;
    --card-white: #f3f3f3;
    --ink-blue: #2a78b6;
    --ink-orange: #e0962f;
    --ink-dark: #1c1c1c;
    --pale-blue: #cfe6f5;
    --icon-orange: #c98f3e;
    --icon-sky: #8fd0e8;
  }
  * { box-sizing: border-box; margin: 0; padding: 0; }
  html, body { width: 1200px; height: 782px; overflow: hidden; }
  body {
    position: relative;
    background: var(--backdrop);
    font-family: "Delius", sans-serif;
  }

  .card {
    position: absolute;
    border-radius: 14px;
    overflow: hidden;
    box-shadow: 0 3px 10px rgba(0,0,0,0.12);
  }

  /* ---------- Back side (blue, shown landscape) ---------- */
  .card-back {
    left: 136px; top: 340px;
    width: 552px; height: 310px;
    background: var(--card-blue);
  }
  .card-back .face {
    position: absolute;
    width: 310px; height: 552px;
    left: 121px; top: -121px;
    transform: rotate(-90deg);
  }
  .brand {
    position: absolute;
    left: 0; width: 100%;
    text-align: center;
  }
  .brand-dot {
    display: block;
    margin: 0 auto 14px;
    border-radius: 50%;
    background: var(--ink-dark);
  }
  .brand-name {
    font-size: 19px;
    line-height: 1.25;
    letter-spacing: 0.04em;
  }
  .card-back .brand { top: 40px; }
  .card-back .brand-dot { width: 92px; height: 92px; }
  .card-back .brand-name { color: #ffffff; }

  .prompt {
    position: absolute;
    left: 34px; top: 322px;
    font-family: "Oxygen", sans-serif;
    font-weight: 300;
    font-size: 21px;
    letter-spacing: 0.16em;
    color: var(--ink-orange);
  }
  .tag-line {
    position: absolute;
    left: 34px; top: 362px;
    font-family: "Oxygen", sans-serif;
    font-size: 13px;
    color: #ffffff;
    letter-spacing: 0.02em;
  }
  .handle {
    position: absolute;
    left: 70px;
    font-family: "Oxygen", sans-serif;
    font-weight: 300;
    font-size: 12px;
    color: var(--pale-blue);
  }
  .handle-hash { top: 388px; }
  .handle-at { top: 408px; }

  .socials {
    position: absolute;
    left: 60px; top: 472px;
    display: flex;
    gap: 26px;
  }
  .social {
    display: flex;
    align-items: center;
    gap: 7px;
    font-size: 13px;
    color: #ffffff;
  }
  .social-square {
    width: 40px; height: 40px;
    border-radius: 6px;
  }
  .social-friendwall .social-square { background: var(--icon-sky); }
  .social-pixlane .social-square { background: var(--icon-orange); }

  /* ---------- Front side (white, portrait) ---------- */
  .card-front {
    left: 710px; top: 84px;
    width: 328px; height: 570px;
    background: var(--card-white);
  }
  .card-front .brand { top: 50px; }
  .card-front .brand-dot { width: 110px; height: 110px; }
  .card-front .brand-name { color: var(--ink-dark); font-size: 20px; }

  .rule {
    position: absolute;
    left: 50px; width: 228px; height: 2px;
    background: linear-gradient(90deg, rgba(224,150,47,0.2), var(--ink-orange) 30%, var(--ink-orange) 70%, rgba(224,150,47,0.2));
  }
  .rule-top { top: 350px; }
  .rule-bottom { top: 540px; }

  .contact {
    position: absolute;
    left: 0; width: 100%; top: 360px;
    text-align: center;
    color: var(--ink-blue);
  }
  .person-name {
    font-family: "Oxygen", sans-serif;
    font-size: 26px;
    letter-spacing: 0.08em;
    line-height: 1.2;
  }
  .person-role {
    font-size: 14px;
    color: var(--ink-orange);
    letter-spacing: 0.06em;
    margin-bottom: 8px;
  }
  .address p {
    font-size: 15px;
    line-height: 22px;
  }
  .lines { margin-top: 10px; }
  .lines p {
    font-size: 14.5px;
    line-height: 22px;
  }
  .lines .label { color: var(--ink-orange); }
</style>
</head>
<body>

  <section class="card card-back" aria-label="Card back">
    <div class="face">
      <div class="brand">
        <span class="brand-dot"></span>
        <p class="brand-name">Kestrel Point<br>Wildland Tours</p>
      </div>
      <p class="prompt">TAKING PICTURES?</p>
      <p class="tag-line">TAG US IN YOUR PICTURES WITH:</p>
      <p class="handle handle-hash">#kpwildtours</p>
      <p class="handle handle-at">@kpwildtours</p>
      <div class="socials">
        <span class="social social-friendwall"><span class="social-square"></span>Friendwall</span>
        <span class="social social-pixlane"><span class="social-square"></span>Pixlane</span>
      </div>
    </div>
  </section>

  <section class="card card-front" aria-label="Card front">
    <div class="brand">
      <span class="brand-dot"></span>
      <p class="brand-name">Kestrel Point<br>Wildland Tours</p>
    </div>
    <span class="rule rule-top"></span>
    <div class="contact">
      <h1 class="person-name">Colin Warbeck</h1>
      <p class="person-role">Director</p>
      <div class="address">
        <p>PO Box 71</p>
        <p>Marlin Cove NSW 2471</p>
      </div>
      <div class="lines">
        <p><span class="label">P:</span> +61 2 5550 1847</p>
        <p><span class="label">E:</span> info@kestrelpointtours.com</p>
        <p><span class="label">W:</span> www.kestrelpointtours.com</p>
      </div>
    </div>
    <span class="rule rule-bottom"></span>
  </section>

</body>
</html>
```